Menu: A4 (double sided) Lunch/Dinner Menu (one side) + Pizza Menu (other side)

Hello.
We would like to create a new style of menus.
Must be easy to read - a summer feel, crisp, clean, beachy, possible retro feel, colours probably based on our website colours (see address below).
Simple and casual is best as we are a casual beachside Cafe.
This menu will be double sided therefore this job is 2 pages.
If you win this job we will have 2 or 3 more menus for you to create soon after (Drinks, Breakfast, possibly a small Kids menu).
The paper for these menus we expect will be a nice white paper which will then be matte laminated.
Colours possible are the green colour #3a6066, the terracotta on our website logo border and website buttons, maybe a little yellow but must be easy to read on white paper.
Black for text might be okay if this is your best design option.
Please view our website and take a feel for the business, location, the existing website branding and website colours we are trying to achieve, www.tidelinekitchen.com.au
We prefer to avoid overwhelming the guest with too many colours on the menus (hence the white paper) as the building is so colourful (El Prado, Argentina, inspired) and the guest experience can be complimented via crisp easy to read menus.
IMPORTANT:
The menus provided please must be fully and easily editable by us in the future.
If you win the job, you must please provide clear instructions on how our staff can edit the menus in the future if project is delivered in Adobe format. Word is also an option for us if you like.
As such, we have attached some documents: the 2x Word documents for the text, 2x .pdf so you can see the fonts and style we were using previously (was printing on recycled brown paper then matte laminated).
If you wished to use the SeaLife Font (this is the existing Font for headings) please let us know as we purchased that font and can provide it.
We have also attached a menu from Marlowe Tavern which we feel has a nice retro feel.
Please include our Instagram in 1 place on the menu @tidelinekitchen
Finally, please note,
we never wish to waste anyone's time so we will narrow down the submissions quickly based on first drafts (please know this is because we appreciate your effort and know your time is valuable) and we will then work with the top designer to finalise in a professional fashion.
Thank you.

```html
<!DOCTYPE html>
<html lang="en">
<head>
<meta charset="utf-8">
<title>Tideline Kitchen – Lunch + Dinner and Pizza Menus</title>
<link rel="stylesheet" href="https://fonts.googleapis.com/css2?family=Alegreya:ital,wght@0,400;0,700;0,800;0,900;1,400;1,700&display=swap">
<style>
:root{
  --teal:#3a6066;
  --ink:#1b1b1b;
  --chilli:#d42a1c;
  --gfo:#1f4fa6;
  --paper:#ffffff;
  --backdrop:#2b2b2b;
  --sketch:#e4e4e4;
}
*{margin:0;padding:0;box-sizing:border-box}
html,body{width:1200px;height:796px;overflow:hidden}
body{background:var(--backdrop);font-family:"Alegreya",Georgia,serif;color:var(--ink);position:relative}
.page{position:absolute;top:82px;width:450px;height:630px;background:var(--paper)}
.page--lunch{left:115px}
.page--pizza{left:635px}
.frame{position:absolute;left:14px;top:13px;width:422px;height:603px;border:1.5px dashed var(--teal)}
.brand{position:absolute;left:144px;top:0;width:161px;height:62px;background:var(--teal);display:flex;flex-direction:column;align-items:center;justify-content:center;color:#fff;font-weight:900;font-size:17px;line-height:1;letter-spacing:.5px;text-transform:uppercase}
.page-title{position:absolute;left:0;width:100%;top:67px;text-align:center;font-weight:800;font-size:30px;letter-spacing:1px;line-height:1}
.legend{position:absolute;left:0;width:100%;text-align:center;font-size:8.5px}
.legend span{margin:0 10px}
.legend span span{margin:0}
.veg{color:var(--chilli);font-weight:700;font-style:italic;font-size:.85em;text-transform:none}
.gfo{color:var(--gfo);font-weight:700;font-size:.75em;text-transform:none}
.ribbon{position:absolute;height:20px}
.ribbon svg{position:absolute;left:0;top:0;width:100%;height:100%;overflow:visible}
.ribbon h2{position:relative;text-align:center;color:var(--teal);font-weight:900;font-size:13.5px;line-height:20px;letter-spacing:.8px}
.divider{position:absolute;width:0;border-left:1px solid var(--ink)}
.item{position:absolute}
.item .name{font-weight:800;font-size:8.8px;line-height:1.05}
.item .name.caps{text-transform:uppercase;font-weight:900;font-size:9px;letter-spacing:.3px}
.item .desc{font-style:italic;font-size:5.7px;line-height:1.4;margin-top:2px;padding-right:30px}
.item .desc.lg{font-size:7px}
.item .price{position:absolute;right:0;top:0;font-weight:700;font-size:9.5px}
.addon{position:absolute;font-weight:700;font-size:6.3px}
.addon .price{position:absolute;right:0;top:-1px;font-size:9.5px;font-weight:700}
.platter{position:absolute;left:60px;width:330px;top:429px;text-align:center}
.platter h3{color:var(--teal);font-weight:900;font-size:10px}
.platter p{font-style:italic;font-size:5.7px;line-height:1.4}
.note{font-size:3.5px;font-style:italic;margin-top:1px}
.handle{position:absolute;left:0;width:100%;top:597px;display:flex;justify-content:center;align-items:center;gap:4px;color:var(--teal);font-weight:700;font-size:7.5px}
.handle i{width:9px;height:9px;border:1.3px solid var(--teal);border-radius:50%}
.allergy{position:absolute;left:34px;width:382px;top:131px;text-align:center;font-size:6.7px;line-height:1.35}
.allergy b{color:var(--chilli);font-weight:400}
.sides{position:absolute;left:0;width:100%;top:169px;display:flex;justify-content:center;align-items:center;gap:9px;font-weight:900;font-size:9.5px;letter-spacing:.3px}
.sides i{display:inline-block;width:16px;border-top:1px solid var(--ink)}
.sketch{position:absolute;background:var(--sketch);border-radius:50%}
.chilli{display:inline-block;width:8px;height:8px;vertical-align:-1px}
.mild{font-size:4.5px;font-weight:400;text-transform:none}
</style>
</head>
<body>
<svg width="0" height="0" style="position:absolute" aria-hidden="true">
  <defs>
    <symbol id="chilli-mark" viewBox="0 0 10 10"><path d="M8.5 1.2 Q9.6 .4 9.8 1.6 Q8.8 2 8.3 2.6 Q6 7.5 1 9.2 Q4.8 6 6.8 2.4 Q7.4 1.4 8.5 1.2Z" fill="#d42a1c"/></symbol>
  </defs>
</svg>

<section class="page page--lunch">
  <div class="frame"></div>
  <div class="brand"><span>Tideline</span><span>Kitchen</span></div>
  <h1 class="page-title">LUNCH + DINNER</h1>
  <p class="legend" style="top:103px"><span><span class="veg">v</span> Vegetarian</span><span><span class="gfo">gfo</span> Gluten Friendly Optional, please ask</span></p>

  <div class="ribbon" style="left:120px;width:210px;top:121px"><svg viewBox="0 0 210 20" preserveAspectRatio="none" aria-hidden="true"><path d="M1 1 H209 L197 10 L209 19 H1 L13 10 Z" fill="#fff" stroke="#3a6066" stroke-width="1"/><path d="M13 10 L20 2.5 H190 L197 10 L190 17.5 H20 Z" fill="none" stroke="#3a6066" stroke-width=".7"/></svg><h2>ENTREE</h2></div>
  <div class="divider" style="left:225px;top:152px;height:91px"></div>

  <div class="item" style="left:29px;width:182px;top:153px"><p class="name">Garlic Bread (2) <span class="veg">v</span></p><span class="price">8</span></div>
  <div class="item" style="left:29px;width:182px;top:180px"><p class="name">Salt &amp; Pepper Squid</p><p class="desc lg">w/ thai dipping sauce</p><span class="price">18</span></div>
  <div class="item" style="left:29px;width:182px;top:205px"><p class="name">Duo of Dip <span class="veg">v</span></p><p class="desc">w/ pita</p><span class="price">14</span></div>
  <div class="item" style="left:29px;width:182px;top:231px"><p class="name">Bowl of Chips <span class="veg">v</span></p><p class="desc">w/ tomato sauce</p><span class="price">11</span></div>

  <div class="item" style="left:237px;width:182px;top:153px"><p class="name">Seasoned Wedges <span class="veg">v</span></p><p class="desc">w/ sour cream &amp; sweet chilli</p><span class="price">15</span></div>
  <div class="item" style="left:237px;width:182px;top:180px"><p class="name">Onion Rings (12)</p><p class="desc">beer battered w/ tangy mayo</p><span class="price">13</span></div>
  <div class="item" style="left:237px;width:182px;top:205px"><p class="name">Vietnamese Spring Rolls (3)</p><p class="desc">chicken, home-made</p><span class="price">11</span></div>
  <div class="item" style="left:237px;width:182px;top:231px"><p class="name">Bruschetta (1) <span class="veg">v</span></p><p class="desc">w/ olive oil, tomato &amp; red onion salsa balsamic glaze, feta</p><span class="price">10</span></div>

  <div class="ribbon" style="left:120px;width:210px;top:261px"><svg viewBox="0 0 210 20" preserveAspectRatio="none" aria-hidden="true"><path d="M1 1 H209 L197 10 L209 19 H1 L13 10 Z" fill="#fff" stroke="#3a6066" stroke-width="1"/><path d="M13 10 L20 2.5 H190 L197 10 L190 17.5 H20 Z" fill="none" stroke="#3a6066" stroke-width=".7"/></svg><h2>MAINS</h2></div>
  <div class="divider" style="left:225px;top:293px;height:122px"></div>

  <div class="item" style="left:29px;width:182px;top:298px"><p class="name caps">The Fish &amp; Chips</p><p class="desc" style="margin-top:4px">house-crumbed butterfish w/ chips,<br>tartare &amp; side salad</p><span class="price">25</span></div>
  <div class="item" style="left:29px;width:182px;top:338px"><p class="name caps">Salt &amp; Pepper Squid</p><p class="desc" style="margin-top:4px">golden tangles w/ chips, thai dipping sauce &amp; side salad</p><span class="price">31</span></div>
  <div class="item" style="left:29px;width:182px;top:378px"><p class="name caps">Smokey Beef &amp; Bacon<br>Cheese Burger</p><p class="desc">w/ chips, onion rings, gerkins &amp; tangy mayo</p><span class="price" style="top:8px">23</span></div>
  <div class="addon" style="left:29px;width:182px;top:406px">+ Jalapenos / + pineapple<span class="price">2</span></div>

  <div class="item" style="left:237px;width:182px;top:298px"><p class="name caps">Atlantic Salmon</p><p class="desc" style="margin-top:4px">served w/ mash, teriyaki sauce &amp; winter vegetables</p><span class="price">31</span></div>
  <div class="item" style="left:237px;width:182px;top:338px"><p class="name caps">Seafood Basket</p><p class="desc" style="margin-top:4px">crumbed butterfish, grilled prawns, salt &amp; pepper squid,<br>chips, tartare &amp; side salad</p><span class="price">31</span></div>
  <div class="item" style="left:237px;width:182px;top:379px"><p class="name caps">Chicken Parmigiana</p><p class="desc" style="margin-top:3px">house-crumbed breast schnitzel, napoli sauce,<br>mozzarella, chips &amp; side salad</p><span class="price">31</span></div>
  <div class="addon" style="left:237px;width:182px;top:409px;font-size:5.8px">+ Bacon And Pineapple / + Jalapenos And Pineapple<span class="price">4</span></div>

  <div class="platter"><h3>TIDELINE PLATTER for 2</h3><p>beer battered flathead, salt &amp; pepper squid, prawn skewers, grilled chicken, lamb &amp; chorizo, served with antipasto, dipping<br>sauces, pita &amp; garlic bread&nbsp; 90 &nbsp;&nbsp;&nbsp;(+45 pp)</p></div>

  <div class="item" style="left:27px;width:184px;top:476px"><p class="name caps">New York Sirloin <span class="gfo">gfo</span></p><p class="desc" style="margin-top:1px">400g msa w/ mash &amp; winter vegetables</p><p class="addon" style="position:static;font-size:5.8px;line-height:1.3">Choose: mushroom gravy or<br>classic gravy&nbsp; or&nbsp; surf ‘n’ turf <span class="gfo">gfo</span></p><p class="note">Please allow 35+ minutes for “well-done”</p><span class="price">38</span><span class="price" style="top:24px">6</span></div>
  <div class="item" style="left:27px;width:184px;top:528px"><p class="name caps">Chicken Caesar</p><p class="desc" style="margin-top:3px">W/ bacon, anchovies, egg, caesar dressing, parmesan,<br>spanish onion, garlic bread</p><span class="price">27</span></div>
  <div class="item" style="left:27px;width:184px;top:562px"><p class="name caps">Lamb Salad <span class="gfo">gfo</span></p><p class="desc" style="margin-top:3px">Skewers w/ traditional <b>greek</b> salad, tzatziki &amp; garlic bread</p><span class="price">30</span></div>
  <div class="addon" style="left:105px;width:106px;top:583px;font-size:6.5px">+ Extra lamb<span class="price">8</span></div>

  <div class="item" style="left:238px;width:183px;top:476px"><p class="name caps">Thai Chicken Curry <svg class="chilli" aria-hidden="true"><use href="#chilli-mark"/></svg><span class="mild"> Mild</span> &nbsp;<span class="gfo">gfo</span></p><p class="desc">Traditional Recipe, W/ Jasmine Rice &amp; Papadums</p><span class="price">26</span></div>
  <div class="item" style="left:238px;width:183px;top:519px"><p class="name caps">Beach Burger <span class="veg">v</span></p><p class="desc" style="margin-top:3px">House-made pea &amp; corn ricotta fritter, pineapple, w/<br>wedges, onion rings, sweet chilli</p><span class="price">23</span></div>
  <div class="item" style="left:238px;width:183px;top:559px"><p class="name caps">Vegan Curry <svg class="chilli" aria-hidden="true"><use href="#chilli-mark"/></svg><span class="mild"> Mild</span> &nbsp;<span class="gfo">gfo</span> <span class="veg">v</span></p><p class="desc" style="margin-top:3px">Chickpea &amp; pumpkin w/ fresh tomatoes &amp; basil,<br>jasmine rice &amp; papadums</p><span class="price">24</span></div>

  <p class="handle"><i></i>@tidelinekitchen</p>
</section>

<section class="page page--pizza">
  <div class="frame"></div>
  <div class="brand"><span>Tideline</span><span>Kitchen</span></div>
  <div class="sketch" role="img" aria-label="Line sketch of a whole pizza with a slice cut out" style="left:39px;top:33px;width:59px;height:73px"></div>
  <div class="sketch" role="img" aria-label="Line sketch of a pizza slice with melting cheese" style="left:329px;top:34px;width:84px;height:67px;border-radius:40% 40% 10% 50%"></div>
  <h1 class="page-title">PIZZA</h1>
  <p class="legend" style="top:98px;font-weight:700;font-size:9.5px">All 12” With House-made Tomato Base &amp; Mozzarella</p>
  <p class="legend" style="top:114px;font-size:7.5px"><span><span class="veg">v</span> Vegetarian</span><span>Gluten Free base <b>+$4</b></span><span>Vegan Cheese <b>+$3</b></span></p>
  <p class="allergy"><b>Allergies? Please let us know!</b> All care is taken to cater for allergies including gluten, however our kitchen is small<br>and we do not have separate preparation or cooking areas. As such, there is risk of cross-contact with your allergen<br>and we are unable to guarantee allergen-free meals. Olives may very rarely contain pips.</p>
  <p class="sides"><span>GARLIC BREAD 8</span><i></i><span>GREEK SALAD 16</span><i></i><span>GARDEN SALAD 12</span></p>

  <div class="ribbon" style="left:116px;width:215px;top:193px"><svg viewBox="0 0 210 20" preserveAspectRatio="none" aria-hidden="true"><path d="M1 1 H209 L197 10 L209 19 H1 L13 10 Z" fill="#fff" stroke="#3a6066" stroke-width="1"/><path d="M13 10 L20 2.5 H190 L197 10 L190 17.5 H20 Z" fill="none" stroke="#3a6066" stroke-width=".7"/></svg><h2>STANDARD</h2></div>
  <div class="divider" style="left:224px;top:224px;height:176px"></div>

  <div class="item" style="left:43px;width:152px;top:225px"><p class="name caps">Hawaiian</p><p class="desc lg" style="margin-top:0">ham, pineapple</p><span class="price">22</span></div>
  <div class="item" style="left:43px;width:152px;top:257px"><p class="name caps">Margherita <span class="veg">v</span></p><p class="desc lg" style="margin-top:0">marinated &amp; diced tomatoes, fresh basil</p><span class="price">22</span></div>
  <div class="item" style="left:43px;width:152px;top:285px"><p class="name caps">BBQ Chicken</p><p class="desc lg" style="margin-top:0">chicken, salami, tomato, spanish<br>onion, bbq sauce</p><span class="price">26</span></div>
  <div class="item" style="left:43px;width:152px;top:322px"><p class="name caps">Chorizo <svg class="chilli" aria-hidden="true"><use href="#chilli-mark"/></svg></p><p class="desc lg" style="margin-top:0">chorizo, salami, tomato, mushrooms<br>spanish onion</p><span class="price">26</span></div>
  <div class="item" style="left:43px;width:152px;top:355px"><p class="name caps">Build Your Own <span class="veg">v</span></p><p class="desc lg" style="margin-top:0">tomato base, mozzarella &amp; four toppings</p><span class="price">26</span></div>
  <div class="item" style="left:43px;width:152px;top:384px"><p class="name caps">Meat Lovers</p><p class="desc lg" style="margin-top:0">chicken, bacon, salami, ham, bbq sauce</p><span class="price">26</span></div>

  <div class="item" style="left:251px;width:153px;top:225px"><p class="name caps">Bella Vista</p><p class="desc lg" style="margin-top:0">chicken, pineapple, ham, spanish<br>onion, mushrooms</p><span class="price">26</span></div>
  <div class="item" style="left:251px;width:153px;top:261px"><p class="name caps">Puttanesca</p><p class="desc lg" style="margin-top:0">anchovies, capers, salami, kalamata olives<br>roasted capsicum, parmesan</p><span class="price">26</span></div>
  <div class="item" style="left:251px;width:153px;top:299px"><p class="name caps">Tropical Chicken <svg class="chilli" aria-hidden="true"><use href="#chilli-mark"/></svg></p><p class="desc lg" style="margin-top:0">chicken, pineapple, spanish onion, chilli<br>tomato, mushrooms</p><span class="price">26</span></div>
  <div class="item" style="left:251px;width:153px;top:337px"><p class="name caps">Vegetarian <span class="veg">v</span></p><p class="desc lg" style="margin-top:0">roasted capsicum, tomato, mushrooms<br>artichokes, kalamata olives, spanish onion</p><span class="price">26</span></div>
  <div class="item" style="left:251px;width:153px;top:374px"><p class="name caps">Tideline Special</p><p class="desc lg" style="margin-top:0;padding-right:0">ham, salami, prawns, kalamata olives,<br>roasted capsicum, mushrooms, spanish onion</p><span class="price">26</span></div>

  <div class="sketch" role="img" aria-label="Line sketch of a pizza in a cast-iron pan" style="left:41px;top:420px;width:52px;height:45px"></div>
  <div class="sketch" role="img" aria-label="Line sketch of a pizza cutter wheel" style="left:349px;top:417px;width:66px;height:34px;border-radius:40%"></div>
  <div class="ribbon" style="left:116px;width:215px;top:431px"><svg viewBox="0 0 210 20" preserveAspectRatio="none" aria-hidden="true"><path d="M1 1 H209 L197 10 L209 19 H1 L13 10 Z" fill="#fff" stroke="#3a6066" stroke-width="1"/><path d="M13 10 L20 2.5 H190 L197 10 L190 17.5 H20 Z" fill="none" stroke="#3a6066" stroke-width=".7"/></svg><h2>GOURMET</h2></div>
  <div class="divider" style="left:224px;top:461px;height:124px"></div>

  <div class="item" style="left:43px;width:152px;top:463px"><p class="name caps">Caveman</p><p class="desc lg" style="margin-top:1px">chicken, lamb, pork sausage, chorizo<br>salami, bacon, spanish onion<br>caramelised onion, smokey bbq sauce</p><span class="price">29</span></div>
  <div class="item" style="left:43px;width:152px;top:511px"><p class="name caps">Spicy Prawn &amp; <svg class="chilli" aria-hidden="true"><use href="#chilli-mark"/></svg><br>Basil Pesto</p><p class="desc lg" style="margin-top:2px">prawns, roasted capsicum, chilli, spring<br>onion, basil pesto</p><span class="price" style="top:8px">29</span></div>
  <div class="item" style="left:43px;width:152px;top:555px"><p class="name caps">Gourmet Vegetarian <span class="veg">v</span></p><p class="desc lg" style="margin-top:0;padding-right:0">pumpkin, eggplant, semi-dried tomatoes<br>roasted capsicum,red onion, bulgarian feta<br>kalamata olives, spinach</p><span class="price">29</span></div>

  <div class="item" style="left:251px;width:153px;top:463px"><p class="name caps">Midnight Rider <svg class="chilli" aria-hidden="true"><use href="#chilli-mark"/></svg><svg class="chilli" aria-hidden="true"><use href="#chilli-mark"/></svg></p><p class="desc lg" style="margin-top:1px">chilli jam, jalapeno peppers, mushrooms<br>bacon, chilli, chorizo, spanish onion</p><span class="price">29</span></div>
  <div class="item" style="left:251px;width:153px;top:500px"><p class="name caps">Lamb Pizza</p><p class="desc lg" style="margin-top:0">lamb, red onion, fresh tomato, tzatziki<br>spring onion</p><span class="price">29</span></div>
  <div class="item" style="left:251px;width:153px;top:534px"><p class="name caps">Pollo Verde</p><p class="desc lg" style="margin-top:0">chicken, pumpkin, basil pesto, spinach<br>feta, pine nuts</p><span class="price">29</span></div>
  <div class="item" style="left:251px;width:153px;top:569px"><p class="name caps">Seafood Pizza</p><p class="desc lg" style="margin-top:0">array of seafood</p><span class="price">29</span></div>

  <p class="handle"><i></i>@tidelinekitchen</p>
</section>
</body>
</html>
```